Need exciting and bold trade show booth design

We focus on Roofing, Siding, Gutters.
We do both retail & insurance (Storm Damage) work. We offer financing.
We are an Halvern Brisk Preferred Contractor.
The following are just my thoughts:
Maybe have half of the backdrop to focus on insurance and half to focus on retail. Maybe have one side white with blue letters and one side white with blue letters? Maybe have the logo in the ,middle to separate the two sides? On the storm damage side have a storm and on the retail side have a calm sky? I am thank the stand alone display will have explained the warranty? Maybe have the highlight the four small sections won my website..... "Affordable Rates, Quick Response, Experienced Team, Veteran Owned."
5 Displays need graphics
10x10 display
Monitor display - logo with company name and logo only. Maybe a slogan added and/or graphic added.
Podium display - logo with company name or logo only. Maybe slogan added and/or graphic added.
Header Display - logo with name only
Stand alone display - Logo with company name and warranty workmanship information, "LSP". We offer a lifetime workmanship warranty, the "Lantern Shield Pledge". I would like the stand alone banner to display the information about our "LSP" workmanship warranty.
Check out our website for more information.
www.tqmroofers.example.
Target Market(s)
Potential roofing siding and gutter customers
Industry/Entity Type
Roofing
Requirements
Must have
- Veteran Owned & Operated.

```html
<!DOCTYPE html>
<html lang="en">
<head>
<meta charset="utf-8">
<title>Torvale Crest Contracting – Trade Show Graphics</title>
<link rel="stylesheet" href="https://fonts.googleapis.com/css2?family=Poppins:wght@400;500;600;700;800&family=Bebas+Neue&display=swap">
<style>
:root{
  --blue:#1e73be;
  --sky:#1da1e8;
  --navy:#124a86;
  --ink:#2b2c30;
  --red:#e21d24;
  --gold:#f5b50f;
  --cyan:#22c2e6;
  --green:#7cc242;
  --slate:#5d6069;
  --paper:#ffffff;
  --mist:#eef1f5;
}
*{box-sizing:border-box;margin:0;padding:0}
html,body{width:1200px;height:2730px;overflow:hidden}
body{
  position:relative;
  font-family:"Poppins",sans-serif;
  background:linear-gradient(180deg,#7a7a7c 0%,#575759 45%,#3d3d3f 100%);
  color:var(--ink);
}
.section-title{
  position:absolute;color:#fff;font-weight:700;font-size:40px;
  text-align:center;transform:translateX(-50%);white-space:nowrap;
}
.panel{position:absolute;background:var(--paper);overflow:hidden;box-shadow:0 8px 18px rgba(0,0,0,.35)}
.abs{position:absolute}

/* brand lockup */
.brand{position:absolute;display:flex;align-items:center}
.brand-mark{border-radius:50%;background:var(--blue);flex:none}
.brand-name{color:var(--blue);font-weight:700;line-height:1.02;text-transform:uppercase;letter-spacing:.04em;white-space:nowrap}
.brand.stack{flex-direction:column}
.brand.stack .brand-name{text-align:center}

/* header */
.header-info{right:68px;top:38px;text-align:right;width:300px}
.header-info .company{font-weight:700;font-size:20px;line-height:1.2;color:var(--ink)}
.pill-red{display:inline-block;margin-top:6px;background:var(--red);color:#fff;font-weight:600;font-size:14px;padding:2px 18px;border-radius:12px}
.header-info .url{margin-top:6px;font-size:18px;color:var(--ink)}
.url b{color:var(--sky);font-weight:600}

/* curved display */
.services-list{left:94px;top:206px}
.services-list li{list-style:none;color:#fff;font-weight:700;font-size:23px;letter-spacing:.03em;display:flex;align-items:center;gap:6px;margin-bottom:6px;padding:0 30px 0 2px;background:linear-gradient(90deg,rgba(40,30,110,.75),rgba(40,30,110,0))}
.dot{width:16px;height:16px;border-radius:50%;border:3px solid #fff;flex:none}
.covered-copy{left:470px;top:186px;width:250px;text-align:center;color:#fff}
.covered-copy .lead{font-weight:800;font-size:22px;line-height:1}
.covered-copy .box{display:inline-block;background:#fff;color:var(--blue);font-weight:800;font-size:27px;line-height:1;padding:1px 8px;margin:2px 0 6px}
.covered-copy p{font-weight:600;font-size:14px;line-height:1.3}
.contact-line{left:0;right:0;top:505px;display:flex;justify-content:center;gap:22px;color:#fff;font-weight:600;font-size:27px}
.contact-line .item{display:flex;align-items:center;gap:8px;white-space:nowrap}

/* stand alone */
.proudly{left:0;right:0;top:118px;text-align:center;font-family:"Bebas Neue",sans-serif;font-size:62px;line-height:1;color:var(--sky)}
.slant-band{position:absolute;transform:skewX(-14deg);text-align:center;font-family:"Bebas Neue",sans-serif;color:#fff;line-height:1}
.slant-band span{display:inline-block;transform:skewX(14deg)}
.benefits{left:36px;top:528px}
.benefit{display:flex;align-items:center;height:56px}
.benefit .ico{width:44px;height:44px;border-radius:50%;background:#fff;display:flex;align-items:center;justify-content:center;flex:none}
.benefit .rule{width:2px;height:42px;background:#fff;margin:0 18px 0 22px}
.benefit p{color:#fff;font-weight:600;font-size:18px;line-height:1.2}
.phone-pill{left:30px;top:769px;height:34px;width:222px;background:var(--gold);border-radius:17px;display:flex;align-items:center;gap:8px;padding-left:4px;color:#fff;font-weight:700;font-size:20px}
.phone-pill .call{width:28px;height:28px;border-radius:50%;background:var(--blue);display:flex;align-items:center;justify-content:center}

/* monitor stand */
.dash-frame{position:absolute;left:29px;top:33px;width:195px;height:875px;border:2px dashed var(--green)}
.trusted{left:0;right:0;top:122px;text-align:center;font-weight:700;color:var(--ink);font-size:16px;line-height:1.15}
.trusted strong{display:block;font-family:"Bebas Neue",sans-serif;font-weight:400;font-size:25px;color:var(--blue);letter-spacing:.01em}
.url-tag{position:absolute;left:42px;width:172px;height:20px;background:var(--blue);transform:skewX(-14deg);color:#fff;font-weight:600;font-size:11px;text-align:center;line-height:20px}
.url-tag span{display:inline-block;transform:skewX(14deg)}
.shelf{position:absolute;left:0;right:0;height:6px;background:#8a8d92}
.shelf-label{position:absolute;left:0;right:0;text-align:center;font-size:13px;color:#444}
.service-pill{position:absolute;left:56px;width:142px;height:24px;border:2px solid var(--blue);border-radius:12px;text-align:center;color:var(--blue);font-weight:700;font-size:17px;line-height:20px}
.monitor{left:678px;top:1336px;width:336px;height:192px;background:#1b1b1d;border-radius:3px;padding:5px 5px 10px}

/* podium */
.podium-box{position:absolute;border:2px dashed var(--green);top:68px;height:261px}
.podium-small{color:#fff;text-align:center;font-weight:600}
</style>
</head>
<body>

<!-- HEADER -->
<div class="section-title" style="left:593px;top:70px">Header Layout</div>
<section class="panel header-layout" style="left:191px;top:136px;width:819px;height:185px">
  <div class="brand" style="left:60px;top:44px;gap:18px">
    <div class="brand-mark" style="width:96px;height:96px"></div>
    <div class="brand-name" style="font-size:34px">Torvale Crest<br>Contracting</div>
  </div>
  <div class="abs header-info">
    <div class="company">TORVALE CREST<br>CONTRACTING SERVICES</div>
    <div class="pill-red">Veteran Owned Small Business</div>
    <div class="url">www.<b>tqmroofers</b>.example</div>
  </div>
</section>

<!-- 10x10 CURVED DISPLAY -->
<div class="section-title" style="left:587px;top:368px">10X10 Curved Display</div>
<section class="panel curved-display" style="left:192px;top:434px;width:816px;height:593px">
  <svg class="abs" width="816" height="593" viewBox="0 0 816 593">
    <defs>
      <linearGradient id="storm" x1="0" y1="0" x2="0" y2="1">
        <stop offset="0" stop-color="#3a2a6e"/><stop offset=".55" stop-color="#8a5aa8"/><stop offset="1" stop-color="#1c1538"/>
      </linearGradient>
      <linearGradient id="sky" x1="0" y1="0" x2="0" y2="1">
        <stop offset="0" stop-color="#3d78c9"/><stop offset=".6" stop-color="#a9c9e8"/><stop offset="1" stop-color="#4b86b8"/>
      </linearGradient>
      <linearGradient id="bgsoft" x1="0" y1="0" x2="1" y2="1">
        <stop offset="0" stop-color="#f1f2f4"/><stop offset="1" stop-color="#ffffff"/>
      </linearGradient>
    </defs>
    <rect width="816" height="593" fill="url(#bgsoft)"/>
    <path role="img" aria-label="Calm blue sky with white clouds over a still lake" fill="url(#sky)"
      d="M816,100 C730,128 650,112 570,160 C480,215 410,268 420,360 C428,420 395,470 382,500 L816,450 Z"/>
    <path role="img" aria-label="Purple storm clouds with lightning striking over a city at night" fill="url(#storm)"
      d="M0,150 C120,160 220,138 310,150 C392,160 418,228 398,305 C380,380 398,440 392,500 C300,482 150,440 0,420 Z"/>
    <path d="M310,150 C392,160 418,228 398,305 C380,380 398,440 392,500" fill="none" stroke="#fff" stroke-width="8"/>
    <path d="M0,430 C150,462 300,500 420,492 C600,478 720,432 816,420 L816,593 L0,593 Z" fill="var(--slate)"/>
    <path d="M0,430 C150,462 300,500 420,492 C600,478 720,432 816,420" fill="none" stroke="#7fb0df" stroke-width="5"/>
    <circle cx="638" cy="118" r="50" fill="#fff"/>
    <circle role="img" aria-label="Veteran owned and operated seal with flag" cx="638" cy="118" r="44" fill="#2a4f9e"/>
  </svg>
  <div class="brand" style="left:236px;top:32px;gap:14px">
    <div class="brand-mark" style="width:84px;height:84px"></div>
    <div class="brand-name" style="font-size:28px">Torvale Crest<br>Contracting</div>
  </div>
  <ul class="abs services-list">
    <li><span class="dot"></span>ROOFING</li>
    <li><span class="dot"></span>SIDING</li>
    <li><span class="dot"></span>GUTTERS</li>
  </ul>
  <div class="abs covered-copy">
    <div class="lead">WE HAVE YOU</div>
    <div class="box">COVERED</div>
    <p>Retail or Insurance<br>Residential or Commercial<br>We have you covered</p>
  </div>
  <div class="abs contact-line">
    <div class="item"><svg width="22" height="22" viewBox="0 0 22 22"><circle cx="11" cy="11" r="9" fill="none" stroke="#1da1e8" stroke-width="2"/><ellipse cx="11" cy="11" rx="4" ry="9" fill="none" stroke="#1da1e8" stroke-width="2"/><line x1="2" y1="11" x2="20" y2="11" stroke="#1da1e8" stroke-width="2"/></svg><span>www.<b style="color:var(--sky);font-weight:600">tqmroofers</b>.example</span></div>
    <div class="item"><svg width="22" height="22" viewBox="0 0 22 22"><circle cx="11" cy="11" r="9" fill="none" stroke="#1da1e8" stroke-width="2"/><path d="M8 6 l2 0 l1 3 l-1.5 1 a6 6 0 0 0 3 3 l1 -1.5 l3 1 l0 2 a2 2 0 0 1 -2 1 a9 9 0 0 1 -7 -7 a2 2 0 0 1 1 -2z" fill="#1da1e8"/></svg><span>855-ROOF-TVC</span></div>
  </div>
</section>

<!-- STAND ALONE DISPLAY -->
<div class="section-title" style="left:385px;top:1076px">Stand Alone Display</div>
<section class="panel stand-alone" style="left:238px;top:1142px;width:281px;height:936px">
  <div class="brand" style="left:22px;top:36px;gap:10px">
    <div class="brand-mark" style="width:62px;height:62px"></div>
    <div class="brand-name" style="font-size:19px">Torvale Crest<br>Contracting</div>
  </div>
  <div class="abs proudly">PROUDLY</div>
  <div class="slant-band" style="left:32px;width:214px;top:178px;height:46px;background:var(--navy);font-size:40px;line-height:48px"><span>OFFERS THE</span></div>
  <div class="abs" role="img" aria-label="Blue umbrella illustration" style="left:50px;top:236px;width:180px;height:100px;border-radius:90px 90px 8px 8px;background:linear-gradient(180deg,#2fa8ee,#1e73be)"></div>
  <div class="slant-band" style="left:44px;width:190px;top:344px;height:40px;background:var(--navy);font-size:40px;line-height:42px"><span>LANTERN</span></div>
  <div class="slant-band" style="left:26px;width:230px;top:384px;height:42px;background:var(--cyan);font-size:40px;line-height:44px"><span>SHIELD</span></div>
  <div class="slant-band" style="left:70px;width:140px;top:426px;height:40px;background:var(--gold);font-size:40px;line-height:42px;color:var(--navy)"><span>PLEDGE</span></div>
  <svg class="abs" style="left:0;top:470px" width="281" height="350" viewBox="0 0 281 350">
    <path d="M0,60 C90,12 190,0 281,0 L281,350 L0,350 Z" fill="var(--blue)"/>
  </svg>
  <div class="abs benefits">
    <div class="benefit"><div class="ico"><span style="color:var(--blue);font-weight:800;font-size:22px">$</span></div><div class="rule"></div><p>Affordable<br>Rates</p></div>
    <div class="benefit"><div class="ico"><svg width="26" height="26" viewBox="0 0 26 26"><path d="M20 18 a8 8 0 1 0 -12 -2" fill="none" stroke="#1e73be" stroke-width="3"/><path d="M3 12 l5 5 l4 -6z" fill="#1e73be"/></svg></div><div class="rule"></div><p>Quick<br>Response</p></div>
    <div class="benefit"><div class="ico"><svg width="28" height="24" viewBox="0 0 28 24"><circle cx="8" cy="7" r="4" fill="#1e73be"/><circle cx="20" cy="7" r="4" fill="#1e73be"/><circle cx="14" cy="10" r="5" fill="#1e73be"/><path d="M3 22 a11 8 0 0 1 22 0z" fill="#1e73be"/></svg></div><div class="rule"></div><p>Experienced<br>Team</p></div>
    <div class="benefit"><div class="ico"><svg width="26" height="20" viewBox="0 0 26 20"><rect width="26" height="20" fill="#1e73be"/><rect y="5" width="26" height="3" fill="#fff"/><rect y="12" width="26" height="3" fill="#fff"/></svg></div><div class="rule"></div><p>Veteran<br>Owned</p></div>
  </div>
  <svg class="abs" style="left:0;top:790px" width="281" height="60" viewBox="0 0 281 60"><path d="M0,0 L281,0 L281,50 C180,20 90,12 0,12 Z" fill="var(--blue)"/></svg>
  <div class="abs phone-pill"><span class="call"><svg width="16" height="16" viewBox="0 0 16 16"><path d="M3 1 l3 0 l1 4 l-2 1 a8 8 0 0 0 5 5 l1 -2 l4 1 l0 3 a2 2 0 0 1 -2 2 a13 13 0 0 1 -12 -12 a2 2 0 0 1 2 -2z" fill="#fff"/></svg></span>855-ROOF-TVC</div>
  <div class="abs" style="left:44px;top:826px;width:80px;height:30px;background:#2f5f9e;border-radius:3px"></div>
  <div class="abs" style="left:138px;top:826px;width:100px;height:30px;background:#e34a4f;border-radius:3px"></div>
  <div class="abs" style="left:0;right:0;top:870px;text-align:center;font-size:18px">www.<b style="color:var(--blue);font-weight:600">tqmroofers</b>.example</div>
</section>

<!-- MONITOR STAND -->
<div class="section-title" style="left:834px;top:1076px">Montior Stand</div>
<section class="panel monitor-stand" style="left:708px;top:1142px;width:254px;height:939px;background:linear-gradient(180deg,#fafafa,#eceef1)">
  <div class="dash-frame"></div>
  <div class="brand" style="left:42px;top:54px;gap:10px">
    <div class="brand-mark" style="width:50px;height:50px"></div>
    <div class="brand-name" style="font-size:16px">Torvale Crest<br>Contracting</div>
  </div>
  <div class="abs trusted">TRUSTED BY<strong>PROPERTY OWNERS</strong>JUST LIKE YOU</div>
  <div class="url-tag" style="top:402px"><span>www.tqmroofers.example</span></div>
  <div class="shelf-label" style="top:504px">SHELF 1</div>
  <div class="shelf" style="top:522px"></div>
  <div class="url-tag" style="top:545px"><span>www.tqmroofers.example</span></div>
  <div class="shelf-label" style="top:642px">SHELF 2</div>
  <div class="shelf" style="top:660px"></div>
  <div class="service-pill" style="top:708px">ROOFING</div>
  <div class="service-pill" style="top:745px">SIDING</div>
  <div class="service-pill" style="top:782px">GUTTERS</div>
  <div class="brand" style="left:48px;top:830px;gap:10px">
    <div class="brand-mark" style="width:46px;height:46px"></div>
    <div class="brand-name" style="font-size:15px">Torvale Crest<br>Contracting</div>
  </div>
</section>
<div class="abs monitor">
  <div role="img" aria-label="Sunset over a calm lake with a wooden pier and a bird in flight" style="width:100%;height:100%;background:linear-gradient(180deg,#8d93c4 0%,#e7b2c2 45%,#c7b9d4 60%,#6f8fb8 100%)"></div>
</div>

<!-- PODIUM -->
<div class="section-title" style="left:609px;top:2128px">Podium Layout</div>
<section class="panel podium" style="left:128px;top:2196px;width:943px;height:396px">
  <svg class="abs" width="943" height="396" viewBox="0 0 943 396">
    <path d="M0,236 C250,188 470,170 560,172 C700,176 840,196 943,236 L943,396 L0,396 Z" fill="var(--blue)"/>
    <path d="M0,228 C250,180 470,162 560,164 C700,168 840,188 943,228" fill="none" stroke="var(--sky)" stroke-width="6"/>
  </svg>
  <div class="podium-box" style="left:182px;width:115px">
    <div class="brand stack" style="left:0;right:0;top:24px;gap:6px">
      <div class="brand-mark" style="width:34px;height:34px"></div>
      <div class="brand-name" style="font-size:11px">Torvale<br>Crest</div>
    </div>
    <div class="abs podium-small" style="left:0;right:0;top:140px;font-size:7px">TORVALE CREST<br>CONTRACTING SERVICES</div>
    <div class="abs podium-small" style="left:0;right:0;top:186px;font-size:10px">855-ROOF-TVC</div>
    <div class="abs podium-small" style="left:0;right:0;top:218px;font-size:10px">tqmroofers.example</div>
  </div>
  <div class="podium-box" style="left:341px;width:261px">
    <div class="brand" style="left:44px;top:24px;gap:10px">
      <div class="brand-mark" style="width:50px;height:50px"></div>
      <div class="brand-name" style="font-size:16px">Torvale Crest<br>Contracting</div>
    </div>
    <div class="abs podium-small" style="left:0;right:0;top:132px;font-size:18px;font-weight:700;line-height:1.2">RESIDENTIAL AND<br>COMMERCIAL</div>
    <div class="abs" style="left:62px;right:62px;top:186px;height:1px;background:#fff"></div>
    <div class="abs podium-small" style="left:0;right:0;top:198px;font-size:16px">&#9742; 855-ROOF-TVC</div>
    <div class="abs podium-small" style="left:36px;right:36px;top:226px;font-size:11px;border:1px solid #fff;border-radius:10px;letter-spacing:.1em">www.tqmroofers.example</div>
  </div>
  <div class="podium-box" style="left:647px;width:113px">
    <div class="brand stack" style="left:0;right:0;top:24px;gap:6px">
      <div class="brand-mark" style="width:34px;height:34px"></div>
      <div class="brand-name" style="font-size:11px">Torvale<br>Crest</div>
    </div>
    <div class="abs podium-small" style="left:0;right:0;top:140px;font-size:7px">TORVALE CREST<br>CONTRACTING SERVICES</div>
    <div class="abs podium-small" style="left:0;right:0;top:186px;font-size:10px">855-ROOF-TVC</div>
    <div class="abs podium-small" style="left:0;right:0;top:218px;font-size:10px">tqmroofers.example</div>
  </div>
</section>

</body>
</html>
```